I need to redesign this website. Modern Fun Professional Redesign For www.JollyPerkHub.com = New Name www.ClaimVouchly.com

Use existing content as it is on website exactly and we will revise after initial mock ups.

The new name will be ClaimVouchly.com please make a quick logo for this site too while redesigning.

Make it look like an official website....

Target Market(s)

Consumers that are redeeming certificates that businesses gave to them as a gift for customer loyalty,e tc.

Industry/Entity Type

It Professional

Logo Text

www.ClaimVouchly.com

Number of Pages Required

4 page

Colors

Designer to choose colors to be used in the design.

Requirements
Must have
• Must look professional, build trust and credibility.
Nice to have
• open
Should not have
• open

```html
<!DOCTYPE html>
<html lang="en">
<head>
<meta charset="utf-8">
<title>ClaimVouchly.com – Welcome To The Redemption Source</title>
<link href="https://fonts.googleapis.com/css2?family=Source+Sans+3:wght@400;600;700&display=swap" rel="stylesheet">
<style>
:root{
  --orange:#f7941d;
  --orange-deep:#ef7d14;
  --blue:#3aa6dd;
  --footer-blue:#2aa3e1;
  --ink:#1c1c1c;
  --white:#ffffff;
  --hero-a:#a8977a;
  --hero-b:#cdbf9f;
  --hero-c:#8c7b62;
}
*{margin:0;padding:0;box-sizing:border-box}
html,body{width:1200px;height:2922px;overflow:hidden;background:var(--white)}
body{position:relative;font-family:"Source Sans 3",sans-serif;color:var(--ink)}
.abs{position:absolute}

/* header */
.site-header{position:absolute;left:0;top:0;width:1200px;height:101px;background:var(--white)}
.brand{position:absolute;left:39px;top:36px;display:flex;align-items:center;gap:8px;font-weight:700;font-size:25px;color:var(--blue)}
.brand-dot{width:24px;height:24px;border-radius:50%;background:var(--orange)}
.nav a{position:absolute;top:0;height:101px;line-height:108px;font-size:31px;color:var(--orange);text-decoration:none}
.nav .is-active{left:534px;width:144px;background:var(--orange);color:var(--white);text-align:center}
.nav .nav-testimonials{left:705px}
.nav .nav-contact{left:932px}

/* hero */
.hero{position:absolute;left:0;top:101px;width:1200px;height:532px;
  background:radial-gradient(ellipse at 75% 40%,var(--hero-b),transparent 60%),
  radial-gradient(ellipse at 15% 75%,#6f6453,transparent 55%),
  linear-gradient(160deg,var(--hero-b),var(--hero-a) 50%,var(--hero-c))}
.hero-title{left:45px;top:160px;font-size:55px;font-weight:700;color:var(--white);letter-spacing:-1px;text-shadow:0 2px 6px rgba(0,0,0,.45)}
.hero-lead{left:43px;top:284px;font-size:29px;font-weight:700;color:var(--white);letter-spacing:-.5px;text-shadow:0 2px 5px rgba(0,0,0,.5)}
.hero-sub{left:43px;top:333px;font-size:23px;font-weight:700;color:var(--white);letter-spacing:-.5px;text-shadow:0 2px 5px rgba(0,0,0,.5)}
.cert-input{left:43px;top:433px;width:415px;height:46px;background:var(--white);border:0}
.cert-input::after{content:"";position:absolute;left:14px;right:14px;bottom:10px;border-bottom:1px solid #bbb}
.go-btn{left:472px;top:418px}

/* about */
.section-title{position:absolute;font-size:51px;font-weight:400;color:var(--blue);text-decoration:underline;text-decoration-thickness:2px;text-underline-offset:8px;letter-spacing:-1px}
.about-title{left:226px;top:686px}
.about-text{left:62px;top:795px;width:720px;font-size:25px;line-height:43px;color:var(--orange-deep);letter-spacing:-.8px}
.about-text strong{font-weight:700}
.about-art{left:775px;top:623px;width:306px;height:503px;background:radial-gradient(circle at 45% 78%,#fde3c6 0 28%,transparent 29%),linear-gradient(#fff,#fff3e6)}

/* testimonials */
.testi-title{left:457px;top:1232px}
.avatar{position:absolute;top:1417px;width:194px;height:194px}
.avatar-photo{position:absolute;left:14px;top:14px;width:166px;height:166px;border-radius:50%}
.avatar-ring{position:absolute;inset:0;border-radius:50%;border:4px solid var(--orange)}
.quote{position:absolute;top:1700px;width:292px;font-size:26px;line-height:33px;color:var(--ink);letter-spacing:-.5px}
.quote .author{display:block;margin-top:30px;font-weight:700}
.see-more{left:542px;top:2322px;font-size:23px;color:var(--orange);letter-spacing:-.5px}

/* footer */
.site-footer{position:absolute;left:0;top:2408px;width:1200px;height:514px;background:var(--footer-blue);color:var(--white)}
.mail-head{left:53px;top:38px;font-size:17px}
.mail-lines{left:53px;top:80px;font-size:17px;line-height:20px;font-weight:600}
.map{left:53px;top:169px;width:317px;height:306px;background:linear-gradient(135deg,#e3e6df,#cfd8cc 45%,#e8e2d4)}
.help-box{left:428px;top:173px;width:283px;height:76px;background:var(--orange)}
.help-icon{position:absolute;left:6px;top:8px;width:50px;height:60px;border-radius:8px;background:#e27612}
.help-box h4{position:absolute;left:64px;top:8px;font-size:13px;font-weight:700}
.help-box p{position:absolute;left:64px;top:26px;width:212px;font-size:9.5px;line-height:12px}
.form-head{left:700px;top:14px;width:376px;text-align:center;font-size:17px;line-height:19px;font-weight:600}
.field-label{position:absolute;left:753px;font-size:16px}
.field{position:absolute;left:752px;width:283px;height:28px;background:var(--white)}
.captcha{left:752px;top:389px;width:90px;height:30px;background:#dfe3ea;color:#2e3b5c;font-size:22px;font-weight:700;text-align:center;line-height:30px;letter-spacing:1px}
.submit-btn{left:973px;top:406px}
</style>
</head>
<body>

<header class="site-header">
  <div class="brand"><span class="brand-dot"></span>ClaimVouchly.com</div>
  <nav class="nav">
    <a class="is-active" href="#">Home</a>
    <a class="nav-testimonials" href="#">Testimonials</a>
    <a class="nav-contact" href="#">Contact Us</a>
  </nav>
</header>

<section class="hero" role="img" aria-label="Travel photo: world map with binoculars, compass, magnifying glass and a jar of coins"></section>
<h1 class="abs hero-title">Welcome To The Redemption Source</h1>
<p class="abs hero-lead">PLEASE ENTER A VALID CERTIFICATE ID IN THE FORM BELOW</p>
<p class="abs hero-sub">TO REDEEM YOUR CERTIFICATE AND TO VIEW FAQ'S, TERMS AND LOCATIONS.</p>
<div class="abs cert-input"></div>
<svg class="abs go-btn" width="84" height="84" viewBox="0 0 84 84">
  <g stroke="#f7941d" stroke-width="2">
    <line x1="42" y1="2" x2="42" y2="9"/><line x1="42" y1="75" x2="42" y2="82"/>
    <line x1="2" y1="42" x2="9" y2="42"/><line x1="75" y1="42" x2="82" y2="42"/>
    <line x1="14" y1="14" x2="19" y2="19"/><line x1="65" y1="65" x2="70" y2="70"/>
    <line x1="70" y1="14" x2="65" y2="19"/><line x1="14" y1="70" x2="19" y2="65"/>
  </g>
  <circle cx="42" cy="42" r="30" fill="#f7941d"/>
  <text x="42" y="52" text-anchor="middle" font-family="Source Sans 3, sans-serif" font-weight="700" font-size="28" fill="#fff">Go</text>
</svg>

<h2 class="section-title about-title">Who are we?</h2>
<p class="abs about-text">ClaimVouchly.com is a leading company in travel certificate fulfillment. Our goal is to make it easy for you to redeem your certificate and our philosophy is this:<br><strong>&nbsp;"What good is it to receive a gift certificate if you can't use it?".</strong><br>If you have any questions about how to redeem a certain certificate, please contact us. We are here to help.</p>
<div class="abs about-art" role="img" aria-label="Orange line illustration of hanging light bulbs above a globe"></div>

<h2 class="section-title testi-title">Testimonials</h2>

<div class="avatar" style="left:108px"><div class="avatar-photo" role="img" aria-label="Photo of a couple celebrating their anniversary" style="background:linear-gradient(160deg,#6b4a34,#a07a55 55%,#3e3a3a)"></div><div class="avatar-ring"></div></div>
<div class="avatar" style="left:468px"><div class="avatar-photo" role="img" aria-label="Photo of a guest at a dinner table" style="background:linear-gradient(160deg,#8a4a3a,#5a3a2e 50%,#a8b070)"></div><div class="avatar-ring"></div></div>
<div class="avatar" style="left:842px"><div class="avatar-photo" role="img" aria-label="Photo of an engaged couple on vacation" style="background:linear-gradient(160deg,#cfc8c0,#6a5a52 55%,#2e2a2a)"></div><div class="avatar-ring"></div></div>

<p class="quote" style="left:101px">"We had an amazing time celebrating our 1st wed-ding anniversary. Customer Service was great. They were very prompt in answering our questions and getting back to us when necessary.<br>What a memorable experience!"<span class="author">Marissa T.</span></p>
<p class="quote" style="left:477px">"Hi! This is a picture of my darling taken in Cedar Falls last weekend!<br>We had a great time. Thank you! "<span class="author">Peter W</span></p>
<p class="quote" style="left:834px;width:270px">"I used this trip to go to LA so that my mom can meet my fiancee and my in-laws. We all became together only because I was able to afford this trip with my vacation voucher. I would highly r ecommend to utilize this kind of vacations/opportunitie s fully. We all as a family enjoyed a lot. Also, I was able to spend some quality time with my fiancee."<span class="author">Raveen S.</span></p>

<p class="abs see-more">See more...</p>

<footer class="site-footer">
  <p class="abs mail-head">Mailing Address:</p>
  <p class="abs mail-lines">The Voucher Desk<br>4120 Harbor Crest Ave Ste B #210<br>Bay Ridge, Ca 90215</p>
  <div class="abs map" role="img" aria-label="Street map showing the office location"></div>
  <svg class="abs" style="left:183px;top:270px" width="30" height="40" viewBox="0 0 30 40"><path d="M15 39C15 39 3 22 3 14a12 12 0 0 1 24 0c0 8-12 25-12 25z" fill="#e23b2e"/><circle cx="15" cy="14" r="5" fill="#fff"/></svg>

  <div class="abs help-box">
    <div class="help-icon"></div>
    <h4>Have Questions?</h4>
    <p>We are here to help you redeem your certificate. Feel free to contact us with any questions or suggestions on how we can do our job better.</p>
  </div>

  <p class="abs form-head">Submit Your Information Below And<br>You Will Be Contacted Within 1 Business Day</p>
  <span class="field-label" style="top:56px">Name</span><div class="field" style="top:85px"></div>
  <span class="field-label" style="top:114px">Certificate ID #:</span><div class="field" style="top:136px"></div>
  <span class="field-label" style="top:171px">E-mail</span><div class="field" style="top:191px"></div>
  <span class="field-label" style="top:227px">Phone:</span><div class="field" style="top:249px"></div>
  <span class="field-label" style="top:284px">How May We Assist You?</span><div class="field" style="top:306px;height:68px"></div>
  <div class="abs captcha">whr88</div>
  <span class="field-label" style="top:421px">Enter Security Code Above:</span><div class="field" style="top:446px;width:232px;height:25px"></div>
  <svg class="abs submit-btn" width="100" height="100" viewBox="0 0 100 100">
    <g stroke="#f7941d" stroke-width="2.5">
      <line x1="50" y1="2" x2="50" y2="10"/><line x1="50" y1="90" x2="50" y2="98"/>
      <line x1="2" y1="50" x2="10" y2="50"/><line x1="90" y1="50" x2="98" y2="50"/>
      <line x1="16" y1="16" x2="22" y2="22"/><line x1="78" y1="78" x2="84" y2="84"/>
      <line x1="84" y1="16" x2="78" y2="22"/><line x1="16" y1="84" x2="22" y2="78"/>
    </g>
    <circle cx="50" cy="50" r="37" fill="#f7941d"/>
    <text x="50" y="58" text-anchor="middle" font-family="Source Sans 3, sans-serif" font-weight="700" font-size="23" fill="#fff">Submit</text>
  </svg>
</footer>

</body>
</html>
```